Graphic Design Project

I need to create a graphic design, which needs to be editable for me in Powerpoint... I have attached it a draft of it, but I need to be able to change the text of it. I want it to look more professional

Target Market(s)

Business Executives

Industry/Entity Type

Graphic Design

Requirements
Must have
• Make it look professional; the colors can change; I just need to be able to edit the text in powerpoint or either word

```html
<!DOCTYPE html>
<html lang="en">
<head>
<meta charset="utf-8">
<title>IT Transformation Framework</title>
<link rel="stylesheet" href="https://fonts.googleapis.com/css2?family=Carlito:wght@400;700&display=swap">
<style>
  :root {
    --page: #ffffff;
    --ink: #111111;
    --accent-red: #e8141c;
    --platform-line: #4aa8c0;
    --shadow: rgba(0,0,0,0.28);

    --green-light: #a6e25a; --green-mid: #7cc831; --green-dark: #4f8e1a;
    --orange-light: #ffa24d; --orange-mid: #f07e22; --orange-dark: #b8570e;
    --yellow-light: #ffd84a; --yellow-mid: #f8be0a; --yellow-dark: #c08e00;
    --purple-light: #9677c4; --purple-mid: #73539f; --purple-dark: #4c3470;
    --blue-light: #5cc6e2; --blue-mid: #2fa3c4; --blue-dark: #1d7190;
  }
  html, body {
    margin: 0;
    padding: 0;
    width: 1200px;
    height: 901px;
    overflow: hidden;
    background: var(--page);
  }
  .framework {
    display: block;
    width: 1200px;
    height: 901px;
    font-family: "Carlito", "Calibri", Arial, sans-serif;
  }
  .block-label {
    font-weight: 700;
    font-size: 21px;
    fill: var(--ink);
    text-anchor: middle;
  }
  .block-label.caps { font-size: 20px; }
  .platform { fill: var(--page); stroke: var(--platform-line); stroke-width: 2; }
  .platform-title {
    font-weight: 700;
    font-size: 40px;
    fill: var(--accent-red);
    text-anchor: middle;
    letter-spacing: 0.5px;
  }
  .ground-shadow { fill: url(#groundShade); }

  .green  .top { fill: var(--green-light); }  .green  .side { fill: var(--green-dark); }  .green  .face { fill: url(#faceGreen); }
  .orange .top { fill: var(--orange-light); } .orange .side { fill: var(--orange-dark); } .orange .face { fill: url(#faceOrange); }
  .yellow .top { fill: var(--yellow-light); } .yellow .side { fill: var(--yellow-dark); } .yellow .face { fill: url(#faceYellow); }
  .purple .top { fill: var(--purple-light); } .purple .side { fill: var(--purple-dark); } .purple .face { fill: url(#facePurple); }
  .blue   .top { fill: var(--blue-light); }   .blue   .side { fill: var(--blue-dark); }   .blue   .face { fill: url(#faceBlue); }

  .stop-green-a { stop-color: var(--green-light); }   .stop-green-b { stop-color: var(--green-mid); }
  .stop-orange-a { stop-color: var(--orange-light); } .stop-orange-b { stop-color: var(--orange-mid); }
  .stop-yellow-a { stop-color: var(--yellow-light); } .stop-yellow-b { stop-color: var(--yellow-mid); }
  .stop-purple-a { stop-color: var(--purple-light); } .stop-purple-b { stop-color: var(--purple-mid); }
  .stop-blue-a { stop-color: var(--blue-light); }     .stop-blue-b { stop-color: var(--blue-mid); }
  .stop-shade-a { stop-color: var(--shadow); }        .stop-shade-b { stop-color: rgba(0,0,0,0); }
</style>
</head>
<body>
<svg class="framework" viewBox="0 0 1080 811" xmlns="http://www.w3.org/2000/svg" role="img" aria-label="Pyramid of IT transformation building blocks resting on Managing Change">
  <defs>
    <linearGradient id="faceGreen" x1="0" y1="0" x2="0" y2="1"><stop offset="0" class="stop-green-a"/><stop offset="1" class="stop-green-b"/></linearGradient>
    <linearGradient id="faceOrange" x1="0" y1="0" x2="0" y2="1"><stop offset="0" class="stop-orange-a"/><stop offset="1" class="stop-orange-b"/></linearGradient>
    <linearGradient id="faceYellow" x1="0" y1="0" x2="0" y2="1"><stop offset="0" class="stop-yellow-a"/><stop offset="1" class="stop-yellow-b"/></linearGradient>
    <linearGradient id="facePurple" x1="0" y1="0" x2="0" y2="1"><stop offset="0" class="stop-purple-a"/><stop offset="1" class="stop-purple-b"/></linearGradient>
    <linearGradient id="faceBlue" x1="0" y1="0" x2="0" y2="1"><stop offset="0" class="stop-blue-a"/><stop offset="1" class="stop-blue-b"/></linearGradient>
    <radialGradient id="groundShade" cx="0.5" cy="0.5" r="0.5"><stop offset="0" class="stop-shade-a"/><stop offset="1" class="stop-shade-b"/></radialGradient>
  </defs>

  <!-- Foundation platform -->
  <ellipse class="ground-shadow" cx="515" cy="712" rx="450" ry="14"/>
  <polygon class="platform" points="90,628 940,628 772,698 260,698"/>
  <text class="platform-title" x="515" y="679">MANAGING CHANGE</text>

  <!-- Base row -->
  <g class="block green" transform="translate(110,512)">
    <polygon class="top" points="0,0 36,-37 206,-37 170,0"/>
    <polygon class="side" points="170,0 206,-37 206,73 170,110"/>
    <rect class="face" x="0" y="0" width="170" height="110"/>
    <text class="block-label" x="85" y="34">Customer</text>
    <text class="block-label" x="85" y="65">Engagement</text>
    <text class="block-label" x="85" y="96">Model</text>
  </g>
  <g class="block orange" transform="translate(322,512)">
    <polygon class="top" points="0,0 36,-37 206,-37 170,0"/>
    <polygon class="side" points="170,0 206,-37 206,73 170,110"/>
    <rect class="face" x="0" y="0" width="170" height="110"/>
    <text class="block-label" x="85" y="34">Service-</text>
    <text class="block-label" x="85" y="65">Minded</text>
    <text class="block-label" x="85" y="96">IT Culture</text>
  </g>
  <g class="block yellow" transform="translate(534,512)">
    <polygon class="top" points="0,0 36,-37 206,-37 170,0"/>
    <polygon class="side" points="170,0 206,-37 206,73 170,110"/>
    <rect class="face" x="0" y="0" width="170" height="110"/>
    <text class="block-label" x="85" y="36">Policy,</text>
    <text class="block-label" x="85" y="67">Process &amp;</text>
    <text class="block-label" x="85" y="96">Methodologies</text>
  </g>
  <g class="block purple" transform="translate(750,512)">
    <polygon class="top" points="0,0 36,-37 206,-37 170,0"/>
    <polygon class="side" points="170,0 206,-37 206,73 170,110"/>
    <rect class="face" x="0" y="0" width="170" height="110"/>
    <text class="block-label" x="85" y="49">Meaningful</text>
    <text class="block-label" x="85" y="80">Metrics</text>
  </g>

  <!-- Second row -->
  <g class="block blue" transform="translate(229,392)">
    <polygon class="top" points="0,0 36,-37 206,-37 170,0"/>
    <polygon class="side" points="170,0 206,-37 206,73 170,110"/>
    <rect class="face" x="0" y="0" width="170" height="110"/>
    <text class="block-label" x="85" y="48">Transform IT</text>
    <text class="block-label" x="85" y="79">Team</text>
  </g>
  <g class="block purple" transform="translate(455,392)">
    <polygon class="top" points="0,0 36,-37 206,-37 170,0"/>
    <polygon class="side" points="170,0 206,-37 206,73 170,110"/>
    <rect class="face" x="0" y="0" width="170" height="110"/>
    <text class="block-label" x="85" y="30">Master</text>
    <text class="block-label" x="85" y="61">Relationship</text>
    <text class="block-label" x="85" y="92">Management</text>
  </g>
  <g class="block green" transform="translate(681,392)">
    <polygon class="top" points="0,0 36,-37 206,-37 170,0"/>
    <polygon class="side" points="170,0 206,-37 206,73 170,110"/>
    <rect class="face" x="0" y="0" width="170" height="110"/>
    <text class="block-label" x="85" y="30">Market &amp;</text>
    <text class="block-label" x="85" y="61">Communicate</text>
    <text class="block-label" x="85" y="92">Value</text>
  </g>

  <!-- Third row -->
  <g class="block yellow" transform="translate(357,265)">
    <polygon class="top" points="0,0 36,-37 206,-37 170,0"/>
    <polygon class="side" points="170,0 206,-37 206,73 170,110"/>
    <rect class="face" x="0" y="0" width="170" height="110"/>
    <text class="block-label" x="85" y="30">Maintain IT</text>
    <text class="block-label" x="85" y="61">Operational</text>
    <text class="block-label" x="85" y="92">Excellence</text>
  </g>
  <g class="block orange" transform="translate(593,262)">
    <polygon class="top" points="0,0 36,-37 206,-37 170,0"/>
    <polygon class="side" points="170,0 206,-37 206,73 170,110"/>
    <rect class="face" x="0" y="0" width="170" height="110"/>
    <text class="block-label" x="85" y="29">Create</text>
    <text class="block-label" x="85" y="60">Business</text>
    <text class="block-label" x="85" y="91">Value</text>
  </g>

  <!-- Apex -->
  <g class="block blue" transform="translate(484,138)">
    <polygon class="top" points="0,0 36,-37 206,-37 170,0"/>
    <polygon class="side" points="170,0 206,-37 206,73 170,110"/>
    <rect class="face" x="0" y="0" width="170" height="110"/>
    <text class="block-label caps" x="85" y="47">IT VISION &amp;</text>
    <text class="block-label caps" x="85" y="77">LEADERSHIP</text>
  </g>
</svg>
</body>
</html>
```